Our website, is loosely based on a grant proposal submitted to the Northern Vascular Society last year for a community-based project that could improve the health of the community at large, I have attached this file for your review (underline "loosely). The idea is to create a "patient navigator" a website where patients can both learn and use as a resource for their care. I have been working on the project for some time, but my other responsibilities as a cardiologist have not allowed me time to learn and design a website of this type. Our website is intended for a spanish speaking audience and is in Spanish language. Designs in english will have to be translated. Our name: AcademiaBrisa.com: means a health university: One option is to have the website have a "university" theme. The project calls for: An initial: easy registration process: collecting name, DOB and city. Simplicity is key, many of our patients barely use computers, and this site is meant to make things easier, not complicate them. The web site should work as an extension of the doctors office, so it should be serious, creative, addictive, engaging. Doctors will see the patients in the office then refer them to the website to continue their learning about their conditions. There should be a page where patients can post questions: a panel of doctors: represented with their pictures, (in circles? around the question answered?) titles and small resumes (our "faculty") answers them. Every person that will attach themself to this website will have a title: doctors and nurses will be professors, residents and fellows will be assistant professors, aids can be PA?. The site should have a market place where people can purchase items that doctors recommend including foods, products and devices; here too, we can have a "bookshop". This should have a flexible mechanism for doctors to add their recommendations a patients can have access to them. Very important: there should be a site intended to be a classroom, this is the meat of this protect: where people can watch videos our staff will make to learn about different subjects; the site should keep track of the videos watched by the person and eventually "graduate them". These videos will be created by my staff, and added over time to the site, students should be able to "request" classes (videos). It should have a site where people can input their medications (notebook), have them stored and printed as a list if necessary. And finally it should have a contact and references section. We have set up a relationship with another site that help people count calories: and a link to this should be available. We have a link to our twitter account, This protect is intended to expand, and we hope to establish a long term relationship with the design team to expand it as needed in the future. The site is on PageHarbor and can be seen in its current form at AcademiaBrisa.com . We have had a logo designed with specific colors of the hospital I work with and one plan is to present it to our hospital to adopt our page in it final form. Again, this site is in spanish and intended for a spanish audience.

Target Market(s)

Spanish speaking, late 30s to early 60s audience.

Industry/Entity Type

Community

Number of Pages Required

Font styles to use
Sans Serif

Colors
a64599
fceff5
3277b5

Requirements
Must have
• A simple, accesible look
Nice to have
• Animations, moving parts
Should not have
• English

```html
<!DOCTYPE html>
<html lang="es">
<head>
<meta charset="utf-8">
<title>AcademiaBrisa</title>
<link href="https://fonts.googleapis.com/css2?family=Open+Sans:ital,wght@0,400;0,600;0,700;0,800;1,400&display=swap" rel="stylesheet">
<style>
:root{
  --navy:#1f3b6c;
  --navy-dark:#172e56;
  --pink:#c7317c;
  --pink-soft:rgba(199,49,124,.82);
  --navy-soft:rgba(31,59,108,.85);
  --sky:#3277b5;
  --band:#dfe6ef;
  --ink:#2b2b2b;
  --muted:#6d6d6d;
  --line:#d6d9de;
  --white:#fff;
  --heart:#d52a3b;
}
*{box-sizing:border-box;margin:0;padding:0}
html,body{width:720px;height:1200px;overflow:hidden;background:var(--white)}
body{font-family:"Open Sans",Arial,sans-serif;color:var(--ink);position:relative}
.btn{display:inline-flex;align-items:center;justify-content:center;gap:4px;font-size:7px;font-weight:700;color:var(--white);background:var(--navy);height:12px;padding:0 8px;letter-spacing:.3px;white-space:nowrap}
.btn--pink{background:var(--pink)}
.btn--white{background:var(--white);color:var(--navy)}
.btn--white.pinktext{color:var(--pink)}
.plus{font-weight:800;font-size:9px;line-height:1}

/* header */
.site-header{position:absolute;left:0;top:0;width:720px;height:100px}
.utility{position:absolute;top:0;left:462px;height:13px;display:flex;align-items:center;font-size:6px;color:var(--navy)}
.utility .lang{margin-right:6px}
.flag{width:11px;height:7px;margin-right:4px;display:block}
.utility .util-login{background:var(--pink);color:var(--white);height:13px;padding:0 6px;display:flex;align-items:center;margin-left:6px}
.utility .util-signup{background:var(--navy);color:var(--white);height:13px;padding:0 6px;display:flex;align-items:center}
.brand{position:absolute;left:122px;top:38px;display:flex;align-items:center;gap:6px}
.brand-mark{width:14px;height:14px;border-radius:50%;background:var(--pink)}
.brand-name{font-size:15px;font-weight:700;color:var(--navy)}
.tagline{position:absolute;left:272px;top:28px;width:260px;font-size:7px;font-style:italic;color:var(--muted);line-height:1.35;text-align:center}
.social{position:absolute;left:555px;top:19px;display:flex;gap:4px}
.social span{width:10px;height:10px;border-radius:50%;background:var(--sky)}
.search{position:absolute;left:544px;top:40px;width:52px;height:8px;border:1px solid var(--line);border-radius:4px}
.search svg{position:absolute;right:2px;top:1px}
.main-nav{position:absolute;left:263px;top:62px;display:flex;align-items:flex-end;height:29px}
.main-nav a{font-size:6.5px;color:#8a8a8a;text-decoration:none;padding:0 5px 6px;letter-spacing:.1px;white-space:nowrap}
.main-nav a.active{background:var(--navy);color:var(--white);height:29px;display:flex;flex-direction:column;align-items:center;justify-content:space-between;padding:3px 6px 6px}

/* hero */
.hero{position:absolute;left:0;top:103px;width:720px;height:264px;background:linear-gradient(90deg,#e9dcd4 0%,#dfe8ee 30%,#cfdce6 55%,#e6eef4 80%,#d9e4ec 100%)}
.hero-card{position:absolute;left:460px;top:207px;width:134px;height:68px;background:rgba(255,255,255,.9);text-align:center;padding:5px 6px}
.hero-card h2{font-size:9px;font-weight:800;color:var(--ink);white-space:nowrap}
.hero-card p{font-size:6.5px;color:var(--muted);line-height:1.3;margin:3px 0 0}
.hero-card .btn{position:absolute;left:50%;transform:translateX(-50%);bottom:-6px}

.tiles{position:absolute;left:120px;top:309px;width:480px;height:124px;display:flex}
.tile{flex:1;text-align:center;color:var(--white);padding-top:6px}
.tile--pink{background:var(--pink-soft)}
.tile--navy{background:var(--navy-soft)}
.tile svg{display:block;margin:0 auto;height:48px}
.tile h3{font-size:10px;font-weight:400;margin-top:7px}
.tile p{font-size:7px;line-height:1.3;margin:2px 12px 6px}

/* questions */
.qa{position:absolute;left:120px;top:449px;width:352px}
.section-title{font-size:10px;font-weight:600;color:var(--navy);letter-spacing:.2px;border-bottom:1px solid var(--line);padding-bottom:3px}
.q-item{display:flex;gap:6px;margin-top:8px}
.date{width:19px;height:22px;background:var(--navy);color:var(--white);font-size:6px;font-weight:700;text-align:center;line-height:1.2;padding-top:2px;flex:none}
.date--pink{background:var(--pink)}
.date b{display:block;font-size:6px;border-top:1px solid rgba(255,255,255,.6);margin-top:1px}
.q-text{font-size:5.5px;line-height:1.45;color:var(--muted)}
.q-text strong{color:var(--ink)}
.view-all{position:absolute;left:87px;top:121px;width:133px}

.login-box{position:absolute;left:484px;top:449px;width:116px;height:122px;background:var(--navy);border-radius:3px;padding:4px 6px;color:var(--white)}
.login-box h3{font-size:12px;font-weight:400;text-align:center;border-bottom:1px solid rgba(255,255,255,.3);padding-bottom:3px;margin-bottom:4px}
.field{display:flex;align-items:center;justify-content:space-between;font-size:5px;margin-bottom:4px}
.field span{width:58px;height:8px;background:var(--white)}
.login-box .query{font-size:5px;margin-bottom:2px}
.login-box .lower{display:flex;gap:4px}
.login-box .area{width:54px;height:34px;background:var(--white)}
.login-box .captcha{width:40px;height:11px;background:#eef0f3;border:1px solid #c8ccd2}
.login-box .send{margin-top:6px;width:42px}

/* health */
.health{position:absolute;left:120px;top:600px;width:480px;height:124px}
.health-intro{position:absolute;left:0;top:14px;width:130px}
.health-intro h2{font-size:11px;font-weight:400;color:var(--navy)}
.health-intro h3{font-size:8px;font-weight:700;color:var(--ink);margin-top:2px;white-space:nowrap}
.health-intro p{font-size:7px;color:var(--muted);line-height:1.35;margin-top:3px}
.health-intro .btn{margin-top:7px}
.service{position:absolute;width:170px;display:flex;gap:6px}
.service svg{flex:none}
.service h4{font-size:9.5px;font-weight:400;color:var(--muted)}
.service p{font-size:6.5px;color:var(--muted);line-height:1.3;margin:1px 0 4px}

/* specialists */
.specialists{position:absolute;left:0;top:742px;width:720px;height:198px;background:var(--band)}
.specialists h2{position:absolute;top:10px;width:100%;text-align:center;font-size:13px;font-weight:700;color:var(--navy-dark);letter-spacing:.3px}
.docs{position:absolute;left:120px;top:32px;width:480px;display:flex;justify-content:space-between}
.doc{width:89px;text-align:center}
.doc .photo{height:88px;background:linear-gradient(180deg,#f4f6f8,#d8e0e8);border:2px solid var(--white)}
.doc h4{font-size:7px;font-weight:700;margin-top:5px}
.doc p{font-size:6px;color:var(--muted);line-height:1.3;margin:3px 4px 5px}

/* articles */
.articles{position:absolute;left:120px;top:950px;width:480px}
.articles h2{font-size:13px;font-weight:400;color:var(--sky);letter-spacing:.2px}
.art-row{display:flex;justify-content:space-between;margin-top:6px}
.art{width:74px}
.art .thumb{width:66px;height:44px;background:linear-gradient(135deg,#e9f1f8,#b9d4ea)}
.art h4{font-size:6px;font-weight:700;line-height:1.25;margin-top:6px}
.art p{font-size:5.5px;color:var(--muted);line-height:1.3;margin:3px 0 6px}
.pager{position:absolute;left:277px;top:1090px;display:flex;align-items:center;gap:9px;font-size:8px;color:#9aa0a8}
.pager .arrow{width:17px;height:17px;background:var(--navy);display:flex;align-items:center;justify-content:center}
.pager .cur{color:var(--ink)}
.pager .nums{display:flex;gap:8px;margin:0 8px}

/* footer */
.site-footer{position:absolute;left:0;top:1120px;width:720px;height:80px;background:var(--navy-dark);color:var(--white)}
.f-links{position:absolute;left:124px;top:9px;font-size:6px;line-height:1.6}
.f-links .copy{font-size:5px;margin-top:2px}
.f-address{position:absolute;left:209px;top:9px;font-size:5.5px;line-height:1.3}
.f-address div{display:flex;gap:5px;align-items:center;margin-bottom:6px}
.f-medical{position:absolute;left:344px;top:8px}
.f-medical h4,.f-contact h4{font-size:7px;font-weight:700;margin-bottom:3px}
.thumbs{display:grid;grid-template-columns:repeat(4,22px);gap:4px 4px}
.thumbs span{height:19px;background:linear-gradient(180deg,#e8edf2,#b9c6d4)}
.f-contact{position:absolute;left:484px;top:8px;width:116px}
.f-contact .field span{width:76px;height:7px}
.f-contact .field.msg span{height:12px}
.f-contact .btn{margin-left:38px;height:10px;width:40px}
</style>
</head>
<body>

<header class="site-header">
  <div class="utility">
    <span class="lang">IDIOMA</span>
    <svg class="flag" viewBox="0 0 11 7"><rect width="11" height="7" fill="#c23b3b"/><rect y="1.5" width="11" height="1" fill="#fff"/><rect y="4" width="11" height="1" fill="#fff"/><rect width="5" height="3.5" fill="#27407a"/></svg>
    <svg class="flag" viewBox="0 0 11 7"><rect width="11" height="7" fill="#c8202d"/><rect y="1.8" width="11" height="3.4" fill="#f3c400"/></svg>
    <span class="util-login">ENTRAR</span><span class="util-signup">REGISTRO</span>
  </div>
  <div class="brand"><span class="brand-mark"></span><span class="brand-name">AcademiaBrisa</span></div>
  <p class="tagline">Lorem ipsum dolor sit amet, consectetur adipiscing elit. Etiam sed sodales neque. Nulla vel risus vitae orci pharetra rhoncus</p>
  <div class="social"><span></span><span></span><span></span></div>
  <div class="search"><svg width="6" height="6" viewBox="0 0 6 6"><circle cx="2.5" cy="2.5" r="1.8" fill="none" stroke="#888" stroke-width=".8"/><line x1="3.8" y1="3.8" x2="5.5" y2="5.5" stroke="#888" stroke-width=".8"/></svg></div>
  <nav class="main-nav">
    <a class="active" href="#"><span class="plus">+</span>INICIO</a>
    <a href="#">SERVICIOS</a><a href="#">HORARIOS</a><a href="#">NOTICIAS</a><a href="#">RECURSOS</a><a href="#">VIDEO</a><a href="#">TIENDA</a><a href="#">PREGUNTAS</a><a href="#">CONTACTO</a>
  </nav>
</header>

<section class="hero" role="img" aria-label="Médico sonriente con estetoscopio frente a personal médico desenfocado en una clínica luminosa"></section>
<div class="hero-card">
  <h2>LOREM IPSUM DOLOR SIT</h2>
  <p>Consectetur adipiscing elit. Cras consectetur ultrices diam, in pulvinar sem volutpat vel.</p>
  <span class="btn">LEER MÁS</span>
</div>

<div class="tiles">
  <div class="tile tile--pink">
    <svg viewBox="0 0 48 48" width="48"><path d="M24 42 21 39C10 29 4 24 4 16 4 10 9 5 15 5c3.6 0 7 1.8 9 4.6C26 6.8 29.4 5 33 5c6 0 11 5 11 11 0 8-6 13-17 23z" fill="var(--heart)"/><polyline points="8,22 17,22 20,16 24,28 27,19 29,22 40,22" fill="none" stroke="#fff" stroke-width="1.8"/></svg>
    <h3>Ritmo cardíaco</h3><p>Lorem ipsum dolor sit amet, consectetur adipiscing elit.</p>
    <span class="btn btn--white"><span class="plus">+</span>LEER MÁS</span>
  </div>
  <div class="tile tile--navy">
    <svg viewBox="0 0 48 48" width="48"><path d="M14 6v12a8 8 0 0 0 16 0V6" fill="none" stroke="#fff" stroke-width="2.4"/><path d="M22 26v8a7 7 0 0 0 14 0v-6" fill="none" stroke="#fff" stroke-width="2.4"/><circle cx="36" cy="25" r="4" fill="#fff"/></svg>
    <h3>Revisar síntomas</h3><p>Lorem ipsum dolor sit amet, consectetur adipiscing elit.</p>
    <span class="btn btn--white"><span class="plus">+</span>LEER MÁS</span>
  </div>
  <div class="tile tile--pink">
    <svg viewBox="0 0 48 48" width="48"><rect x="18" y="7" width="12" height="6" rx="2" fill="none" stroke="#fff" stroke-width="2"/><rect x="7" y="12" width="34" height="28" rx="3" fill="#fff"/><rect x="21" y="18" width="6" height="16" fill="var(--heart)"/><rect x="16" y="23" width="16" height="6" fill="var(--heart)"/></svg>
    <h3>Consulta</h3><p>Lorem ipsum dolor sit amet, consectetur adipiscing elit.</p>
    <span class="btn btn--white pinktext"><span class="plus">+</span>LEER MÁS</span>
  </div>
  <div class="tile tile--navy">
    <svg viewBox="0 0 48 48" width="48"><ellipse cx="30" cy="18" rx="14" ry="11" fill="#9cc7ee"/><ellipse cx="19" cy="26" rx="15" ry="12" fill="#4a9be0"/><path d="M10 34l-3 8 10-5z" fill="#4a9be0"/><circle cx="13" cy="26" r="2" fill="#fff"/><circle cx="19" cy="26" r="2" fill="#fff"/><circle cx="25" cy="26" r="2" fill="#fff"/></svg>
    <h3>Ayuda en línea</h3><p>Lorem ipsum dolor sit amet, consectetur adipiscing elit.</p>
    <span class="btn btn--white"><span class="plus">+</span>PREGUNTAR</span>
  </div>
</div>

<section class="qa">
  <h2 class="section-title">PREGUNTAS RESPONDIDAS</h2>
  <div class="q-item"><div class="date date--pink">SÁB<b>14</b></div>
    <p class="q-text"><strong>PREGUNTA:</strong> LOREM IPSUM DOLOR SIT AMET, CONSECTETUR ADIPISCING ELIT?<br><strong>RESPUESTA:</strong> Suspendisse eget tellus a nulla tempor luctus. Sed ac cursus urna, a efficitur justo. Curabitur sed varius quam, non feugiat ligula nec semper massa.</p></div>
  <div class="q-item"><div class="date">SÁB<b>14</b></div>
    <p class="q-text"><strong>PREGUNTA:</strong> LOREM IPSUM DOLOR SIT AMET, CONSECTETUR ADIPISCING ELIT?<br><strong>RESPUESTA:</strong> Suspendisse eget tellus a nulla tempor luctus. Sed ac cursus urna, a efficitur justo. Curabitur sed varius quam, non feugiat ligula nec semper massa.</p></div>
  <div class="q-item"><div class="date date--pink">SÁB<b>14</b></div>
    <p class="q-text"><strong>PREGUNTA:</strong> LOREM IPSUM DOLOR SIT AMET, CONSECTETUR ADIPISCING ELIT?<br><strong>RESPUESTA:</strong> Suspendisse eget tellus a nulla tempor luctus. Sed ac cursus urna, a efficitur justo. Curabitur sed varius quam, non feugiat ligula nec semper massa.</p></div>
  <span class="btn view-all">VER TODAS</span>
</section>

<aside class="login-box">
  <h3>Iniciar sesión</h3>
  <div class="field">Nombre<span></span></div>
  <div class="field">Teléfono móvil<span></span></div>
  <div class="field">Correo electrónico<span></span></div>
  <div class="query">Consulta <em>(su pregunta)</em></div>
  <div class="lower"><div class="area"></div><div><div class="captcha"></div><span class="btn send">ENVIAR</span></div></div>
</aside>

<section class="health">
  <div class="health-intro">
    <h2>SALUD Y MEDICINA</h2>
    <h3>Lorem ipsum dolor sit amet</h3>
    <h3 style="margin-top:0">Donec rutrum ligula eu leo aliquet</h3>
    <p>Etiam tempor magna a con sequat molestie. Morbi faucibus efficitur dolor, at tempus metus fringilla non.</p>
    <span class="btn">VER NUESTROS SERVICIOS</span>
  </div>
  <div class="service" style="left:141px;top:4px">
    <svg width="50" height="44" viewBox="0 0 48 44"><path d="M24 40 21 37C10 27 4 22 4 14 4 8 9 3 15 3c3.6 0 7 1.8 9 4.6C26 4.8 29.4 3 33 3c6 0 11 5 11 11 0 8-6 13-17 23z" fill="var(--heart)"/><polyline points="8,20 17,20 20,14 24,26 27,17 29,20 40,20" fill="none" stroke="#fff" stroke-width="1.8"/></svg>
    <div><h4>Ritmo cardíaco</h4><p>Donec rutrum ligula eu leo aliquet por ta. Etiam tempor magna a consequat.</p><span class="btn"><span class="plus">+</span>LEER MÁS</span></div>
  </div>
  <div class="service" style="left:318px;top:4px">
    <svg width="40" height="44" viewBox="0 0 40 44"><path d="M8 4v12a7 7 0 0 0 14 0V4" fill="none" stroke="#333" stroke-width="2.2"/><path d="M15 23v8a7 7 0 0 0 14 0v-6" fill="none" stroke="#333" stroke-width="2.2"/><circle cx="29" cy="22" r="4" fill="#999"/></svg>
    <div><h4>Revisar síntomas</h4><p>Donec rutrum ligula eu leo aliquet por ta. Etiam tempor magna a consequat.</p><span class="btn"><span class="plus">+</span>LEER MÁS</span></div>
  </div>
  <div class="service" style="left:141px;top:70px">
    <svg width="50" height="44" viewBox="0 0 50 44"><rect x="19" y="6" width="12" height="6" rx="2" fill="none" stroke="#bbb" stroke-width="2"/><rect x="6" y="11" width="38" height="28" rx="3" fill="#f1f2f4" stroke="#d0d3d8"/><rect x="22" y="17" width="6" height="16" fill="var(--heart)"/><rect x="17" y="22" width="16" height="6" fill="var(--heart)"/></svg>
    <div><h4>Consulta</h4><p>Donec rutrum ligula eu leo aliquet por ta. Etiam tempor magna a consequat.</p><span class="btn"><span class="plus">+</span>LEER MÁS</span></div>
  </div>
  <div class="service" style="left:318px;top:70px">
    <svg width="40" height="44" viewBox="0 0 40 44"><rect x="4" y="8" width="26" height="32" rx="3" fill="#f1f2f4" stroke="#d0d3d8"/><rect x="14" y="12" width="4" height="10" fill="var(--heart)"/><rect x="11" y="15" width="10" height="4" fill="var(--heart)"/><rect x="14" y="26" width="14" height="10" rx="2" fill="#999"/><path d="M28 31l8-5v10z" fill="#999"/></svg>
    <div><h4>Ayuda por video</h4><p>Donec rutrum ligula eu leo aliquet por ta. Etiam tempor magna a consequat.</p><span class="btn"><span class="plus">+</span>LEER MÁS</span></div>
  </div>
</section>

<section class="specialists">
  <h2>ESPECIALISTAS MÉDICOS</h2>
  <div class="docs">
    <div class="doc"><div class="photo" role="img" aria-label="Retrato de un cirujano con uniforme verde azulado"></div><h4>Dr. Juan Pérez</h4><p>Lorem ipsum dolor sit amet, consectetur adipiscing elit. Cras consectetur ultrices diam, in</p><span class="btn">LEER MÁS</span></div>
    <div class="doc"><div class="photo" role="img" aria-label="Retrato de una doctora con bata blanca"></div><h4>Dra. Ana Pérez</h4><p>Lorem ipsum dolor sit amet, consectetur adipiscing elit. Cras consectetur ultrices diam, in</p><span class="btn">LEER MÁS</span></div>
    <div class="doc"><div class="photo" role="img" aria-label="Retrato de un médico con bata blanca y corbata"></div><h4>Dr. Juan Pérez</h4><p>Lorem ipsum dolor sit amet, consectetur adipiscing elit. Cras consectetur ultrices diam, in</p><span class="btn">LEER MÁS</span></div>
    <div class="doc"><div class="photo" role="img" aria-label="Retrato de una joven doctora con estetoscopio"></div><h4>Dra. Ana Pérez</h4><p>Lorem ipsum dolor sit amet, consectetur adipiscing elit. Cras consectetur ultrices diam, in</p><span class="btn">LEER MÁS</span></div>
    <div class="doc"><div class="photo" role="img" aria-label="Retrato de un médico mayor con estetoscopio"></div><h4>Dr. Juan Pérez</h4><p>Lorem ipsum dolor sit amet, consectetur adipiscing elit. Cras consectetur ultrices diam, in</p><span class="btn">LEER MÁS</span></div>
  </div>
</section>

<section class="articles">
  <h2>RECOMENDADOS EN ARTÍCULOS MÉDICOS</h2>
  <div class="art-row">
    <div class="art"><div class="thumb" role="img" aria-label="Pastillas blancas sobre una superficie clara"></div><h4>MAURIS LIGULA TURPIS, PORTA AT GRAVIDA</h4><p>Tincidunt eu neque. Aliquam vehicula auctor nibh ac</p><span class="btn btn--pink">LEER MÁS</span></div>
    <div class="art"><div class="thumb" role="img" aria-label="Cápsulas con margaritas sobre fondo azul"></div><h4>MAURIS LIGULA TURPIS, PORTA AT GRAVIDA</h4><p>Tincidunt eu neque. Aliquam vehicula auctor nibh ac</p><span class="btn btn--pink">LEER MÁS</span></div>
    <div class="art"><div class="thumb" role="img" aria-label="Jarabe vertido en una cuchara"></div><h4>MAURIS LIGULA TURPIS, PORTA AT GRAVIDA</h4><p>Tincidunt eu neque. Aliquam vehicula auctor nibh ac</p><span class="btn btn--pink">LEER MÁS</span></div>
    <div class="art"><div class="thumb" role="img" aria-label="Cápsulas con margaritas sobre fondo azul"></div><h4>MAURIS LIGULA TURPIS, PORTA AT GRAVIDA</h4><p>Tincidunt eu neque. Aliquam vehicula auctor nibh ac</p><span class="btn btn--pink">LEER MÁS</span></div>
    <div class="art"><div class="thumb" role="img" aria-label="Pastillas blancas sobre una superficie clara"></div><h4>MAURIS LIGULA TURPIS, PORTA AT GRAVIDA</h4><p>Tincidunt eu neque. Aliquam vehicula auctor nibh ac</p><span class="btn btn--pink">LEER MÁS</span></div>
  </div>
</section>

<div class="pager">
  <span class="arrow"><svg width="7" height="9" viewBox="0 0 7 9"><polyline points="5.5,1 1.5,4.5 5.5,8" fill="none" stroke="#fff" stroke-width="1.6"/></svg></span>
  <span class="nums"><span class="cur">1</span><span>2</span><span>3</span><span>4</span><span>5</span><span>6</span><span>7</span></span>
  <span class="arrow"><svg width="7" height="9" viewBox="0 0 7 9"><polyline points="1.5,1 5.5,4.5 1.5,8" fill="none" stroke="#fff" stroke-width="1.6"/></svg></span>
</div>

<footer class="site-footer">
  <div class="f-links">
    <div>INICIO &nbsp;|&nbsp; SERVICIOS</div>
    <div>HORARIOS &nbsp;|&nbsp; NOTICIAS</div>
    <div>RECURSOS &nbsp;|&nbsp; VIDEO</div>
    <div>TIENDA &nbsp;|&nbsp; PREGUNTAS</div>
    <div>CONTACTO</div>
    <div class="copy">DERECHOS© 2013</div>
  </div>
  <div class="f-address">
    <div><svg width="14" height="12" viewBox="0 0 14 12"><path d="M7 1 1 6h2v5h3V8h2v3h3V6h2z" fill="#fff"/></svg><span>LOREM IPSUM DOLOR SIT AMET,<br>CONSECTETUR ADIPISCING ELIT.</span></div>
    <div><svg width="14" height="12" viewBox="0 0 14 12"><rect x="1" y="2" width="12" height="8" fill="none" stroke="#fff"/><polyline points="1,2 7,7 13,2" fill="none" stroke="#fff"/></svg><span>CONSECTETUR ADIPISCING ELIT.</span></div>
    <div><svg width="14" height="12" viewBox="0 0 14 12"><path d="M3 1h3l1 3-2 1c1 2 2 3 4 4l1-2 3 1v3c-6 0-10-4-10-10z" fill="#fff"/></svg><span>555-014-2290 - 555-017-8834</span></div>
  </div>
  <div class="f-medical">
    <h4>MÉDICOS</h4>
    <div class="thumbs" role="img" aria-label="Cuadrícula de ocho pequeños retratos de médicos">
      <span></span><span></span><span></span><span></span><span></span><span></span><span></span><span></span>
    </div>
  </div>
  <div class="f-contact">
    <h4>CONTÁCTENOS</h4>
    <div class="field">Nombre<span></span></div>
    <div class="field">Correo<span></span></div>
    <div class="field msg">Mensaje<span></span></div>
    <span class="btn">ENVIAR</span>
  </div>
</footer>

</body>
</html>
```